We need a new brochure design for our dental clinic, Briar Dental. We have attached the information we want printed and photos to include.

Industry/Entity Type

Dental

```html
<!DOCTYPE html>
<html lang="en">
<head>
<meta charset="utf-8">
<title>Briar Dental – Trifold Brochure</title>
<link rel="stylesheet" href="https://fonts.googleapis.com/css2?family=Questrial&family=Open+Sans:wght@400;600&display=swap">
<style>
  :root {
    --bg: #5b5d61;
    --blue-deep: #0b5fae;
    --blue: #1a8fdb;
    --blue-light: #3fb0ee;
    --lime: #c8dc12;
    --green: #46b035;
    --green-text: #6cbf2a;
    --white: #ffffff;
    --photo-light: #8fcdf3;
    --photo-dark: #2a3440;
  }
  * { box-sizing: border-box; margin: 0; padding: 0; }
  html, body { width: 1200px; height: 900px; overflow: hidden; }
  body { background: var(--bg); font-family: "Questrial", sans-serif; }

  .brochure {
    position: absolute; left: 60px; top: 70px;
    width: 1080px; height: 760px;
    display: flex;
    box-shadow: 0 12px 40px rgba(0,0,0,.35);
  }
  .panel { position: relative; width: 360px; height: 760px; overflow: hidden; background: var(--white); }

  .blue-field { position: absolute; left: 0; right: 0; bottom: 0; background: linear-gradient(180deg, var(--blue-light) 0%, var(--blue) 45%, var(--blue-deep) 100%); }
  .curve { position: absolute; left: 0; width: 100%; }

  /* panel 1: profile */
  .profile .bio-field { position: absolute; left: 0; top: 0; width: 100%; height: 330px; background: linear-gradient(135deg, var(--lime) 0%, #8cc62a 50%, var(--green) 100%); }
  .profile .bio { position: absolute; left: 26px; top: 34px; right: 26px; font-family: "Open Sans", sans-serif; font-size: 13px; line-height: 1.55; color: var(--white); }
  .profile .bio p + p { margin-top: 12px; }
  .profile .blue-field { top: 300px; }
  .section-title { position: absolute; right: 26px; top: 350px; text-align: right; color: var(--white); font-size: 30px; font-weight: 400; line-height: 1.05; letter-spacing: 1px; }
  .dentist-photo { position: absolute; left: 30px; bottom: 0; width: 300px; height: 300px; border-radius: 24px 24px 0 0; background: linear-gradient(180deg, var(--photo-light) 0%, #4f7fa6 50%, var(--photo-dark) 100%); box-shadow: 0 0 24px rgba(255,255,255,.35); }

  /* panel 2: services */
  .services .clinic-photo { position: absolute; left: 50%; top: 40px; width: 200px; height: 200px; margin-left: -100px; border-radius: 50%; border: 6px solid var(--blue); background: radial-gradient(circle at 40% 40%, #e8f2fa 0%, #9cc3e2 55%, #4f82b6 100%); }
  .services .blue-field { top: 270px; }
  .service-list { position: absolute; left: 40px; top: 320px; list-style: none; color: var(--white); font-size: 21px; line-height: 1.75; }
  .service-list li::before { content: "•"; margin-right: 10px; color: var(--lime); }
  .finance-note { position: absolute; left: 40px; right: 30px; bottom: 46px; color: var(--lime); font-size: 20px; line-height: 1.3; }

  /* panel 3: cover */
  .cover .smile-photo { position: absolute; left: 0; top: 0; width: 100%; height: 200px; background: linear-gradient(90deg, #f3e3dc 0%, #e9b9a5 35%, #e2557f 62%, #f3e3dc 100%); }
  .tagline { position: absolute; left: 0; right: 0; top: 222px; text-align: center; color: var(--green-text); font-size: 27px; font-weight: 400; line-height: 1.2; }
  .cover .blue-field { top: 300px; }
  .brand { position: absolute; left: 40px; top: 420px; display: flex; align-items: center; gap: 18px; color: var(--white); }
  .brand-mark { width: 60px; height: 60px; background: var(--white); border-radius: 10px; }
  .brand-name { font-size: 30px; letter-spacing: 1px; line-height: 1.1; }
  .call-text { position: absolute; left: 0; right: 0; top: 525px; text-align: center; color: var(--white); font-size: 22px; line-height: 1.25; }
  .phone-pill { position: absolute; left: 40px; right: 40px; top: 595px; height: 64px; border-radius: 14px; background: var(--white); display: flex; align-items: center; justify-content: center; gap: 14px; color: var(--blue-deep); font-size: 36px; }
  .phone-pill svg { width: 34px; height: 34px; }
  .email { position: absolute; left: 0; right: 0; bottom: 40px; text-align: center; color: var(--white); font-size: 21px; }
</style>
</head>
<body>
<main class="brochure">

  <section class="panel profile">
    <div class="bio-field">
      <div class="bio">
        <p>Dr Arvin Rao obtained his BDS from the National University in 2006 and served in the public dental service and the armed forces before joining private practice.</p>
        <p>In 2014 he was admitted as a fellow of a leading dental college, with a keen interest in aesthetic and restorative dentistry.</p>
      </div>
    </div>
    <svg class="curve" style="top:270px" width="360" height="80" viewBox="0 0 360 80" preserveAspectRatio="none">
      <path d="M0 80 C120 10 250 0 360 0 L360 30 C250 30 130 40 0 80 Z" fill="#ffffff"/>
    </svg>
    <div class="blue-field"></div>
    <svg class="curve" style="top:270px" width="360" height="80" viewBox="0 0 360 80" preserveAspectRatio="none">
      <path d="M0 60 C120 5 250 0 360 0 L360 14 C250 16 130 30 0 80 Z" fill="#ffffff"/>
    </svg>
    <h2 class="section-title">SERVICE<br>PROVIDED</h2>
    <div class="dentist-photo" role="img" aria-label="Photo of the dentist in dark scrubs with loupes"></div>
  </section>

  <section class="panel services">
    <div class="clinic-photo" role="img" aria-label="Photo of the clinic treatment room"></div>
    <div class="blue-field"></div>
    <ul class="service-list">
      <li>General Dentistry</li>
      <li>Teeth Whitening</li>
      <li>Dental Implants</li>
      <li>Crowns and Bridges</li>
      <li>Root Canal Treatment</li>
      <li>Orthodontics</li>
      <li>Wisdom Tooth Surgery</li>
      <li>Children's Dentistry</li>
    </ul>
    <p class="finance-note">0% interest free installment plans available.</p>
  </section>

  <section class="panel cover">
    <div class="smile-photo" role="img" aria-label="Close-up photo of a bright white smile"></div>
    <div class="blue-field"></div>
    <svg class="curve" style="top:299px" width="360" height="102" viewBox="0 0 360 102" preserveAspectRatio="none">
      <path d="M0 0 H360 V0 C250 40 120 78 0 102 Z" fill="#ffffff"/>
      <path d="M0 102 C120 78 250 40 360 0 V26 C250 60 120 88 0 102 Z" fill="#46b035"/>
    </svg>
    <h1 class="tagline">A Healthier Smile For<br>A Healthier You</h1>
    <div class="brand">
      <span class="brand-mark"></span>
      <span class="brand-name">BRIAR<br>DENTAL</span>
    </div>
    <p class="call-text">Call us for an<br>appointment today.</p>
    <div class="phone-pill">
      <svg viewBox="0 0 24 24" aria-hidden="true"><path fill="#0b5fae" d="M6.6 10.8a15 15 0 0 0 6.6 6.6l2.2-2.2a1 1 0 0 1 1-.25 11.4 11.4 0 0 0 3.6.57 1 1 0 0 1 1 1V20a1 1 0 0 1-1 1A17 17 0 0 1 3 4a1 1 0 0 1 1-1h3.5a1 1 0 0 1 1 1c0 1.25.2 2.45.57 3.57a1 1 0 0 1-.25 1Z"/></svg>
      <span>6123 4567</span>
    </div>
    <p class="email">info@briardental.com.sg</p>
  </section>

</main>
</body>
</html>
```